Vantor Ridged Concrete & Grinding
I'm looking for a business card and logo design for my
new Polished Concrete & Grinding business,
If you were to look up Vantor in the dictionary it would
say, first in importance, order, or position; leading.
Polished Concrete floors are a niche market, that are being used currently in Shopping centres, office spaces and by most high end architects, builders and designers.
i need my business card & logo to stand out from my
competitors, i need my design + logo to reflect this it
needs to be simple, professional, eye catching, easy
to read and scream quality. The logo will need to be
suitable for a whole range of applications including,
uniforms, letter heads, stickers, and eventually
incorporating in vehicle vinyl wrapping.
Target Market(s)
Builders, architects, Interior designers & home owners
Contact Information for Business Card
Front side:
- Vantor Ridged Concrete & Grinding.
- Logo
Rear side:
- Neil Varbusk
- 0491587302
- info@vantorrcg.com.au
- commercial - domestic - industrial
- (later down the line website & space for
social media links
www.vantorridgedconcrete.com.au)
Colors
Designer to choose colors to be used in the design.
Look and feel

```html
<!DOCTYPE html>
<html lang="en">
<head>
<meta charset="utf-8">
<title>Vantor Ridged Concrete &amp; Grinding – Business Card</title>
<link rel="stylesheet" href="https://fonts.googleapis.com/css2?family=Montserrat:wght@500;600;700&family=Open+Sans:wght@400;600&display=swap">
<style>
  :root {
    --backdrop: #2a2a2b;
    --slate: #647b89;
    --slate-dark: #4d6270;
    --slate-light: #7f95a2;
    --charcoal: #3a3536;
    --paper: #f6f6f5;
    --ink: #3b3b3b;
    --band-text: #d9d6d4;
    --white: #ffffff;
  }
  * { margin: 0; padding: 0; box-sizing: border-box; }
  html, body { width: 1200px; height: 900px; overflow: hidden; }
  body {
    background: var(--backdrop);
    display: flex;
    flex-direction: column;
    align-items: center;
    justify-content: center;
    gap: 60px;
  }
  .card {
    position: relative;
    width: 600px;
    height: 343px;
    border-radius: 26px;
    overflow: hidden;
  }

  /* Front */
  .card--front {
    background: radial-gradient(ellipse at 50% 40%, var(--slate-light), var(--slate) 55%, var(--slate-dark));
    display: flex;
    align-items: center;
    justify-content: center;
  }
  .brand { text-align: center; }
  .brand__name {
    font-family: "Montserrat", sans-serif;
    font-weight: 700;
    letter-spacing: 2px;
    line-height: 1;
  }
  .brand__tagline {
    font-family: "Montserrat", sans-serif;
    font-weight: 600;
    text-transform: uppercase;
    letter-spacing: 1.6px;
    margin-top: 6px;
  }
  .card--front .brand__name { color: var(--white); font-size: 54px; }
  .card--front .brand__tagline { color: var(--white); font-size: 11px; }

  /* Back */
  .card--back { background: var(--paper); }
  .card--back .brand {
    position: absolute;
    top: 48px;
    right: 40px;
  }
  .card--back .brand__name { color: var(--slate); font-size: 36px; }
  .card--back .brand__tagline { color: var(--slate); font-size: 7.5px; margin-top: 4px; }

  .holder {
    position: absolute;
    top: 112px;
    left: 0;
    display: flex;
    align-items: center;
    gap: 30px;
  }
  .holder__marker { width: 16px; height: 30px; background: var(--slate); }
  .holder__name {
    font-family: "Montserrat", sans-serif;
    font-weight: 700;
    font-size: 20px;
    color: var(--slate);
    text-transform: uppercase;
    letter-spacing: 0.5px;
  }

  .bands { position: absolute; left: 0; top: 0; }

  .contacts {
    position: absolute;
    left: 60px;
    top: 160px;
    list-style: none;
    font-family: "Open Sans", sans-serif;
    font-size: 15px;
    color: var(--ink);
  }
  .contacts li {
    display: flex;
    align-items: center;
    gap: 10px;
    height: 22px;
    margin-bottom: 2px;
  }
  .contacts svg { flex: none; }

  .sectors {
    position: absolute;
    right: 28px;
    top: 240px;
    line-height: 18px;
    font-family: "Open Sans", sans-serif;
    font-size: 14px;
    color: var(--band-text);
    text-transform: uppercase;
    letter-spacing: 0.3px;
  }
  .social {
    position: absolute;
    left: 36px;
    top: 268px;
    display: flex;
    align-items: center;
    gap: 6px;
    font-family: "Open Sans", sans-serif;
    font-size: 14px;
    color: var(--white);
  }
  .social__chip { width: 14px; height: 14px; background: var(--white); border-radius: 2px; }
  .social__handle { margin-left: 6px; }
</style>
</head>
<body>

  <section class="card card--front" aria-label="Card front">
    <div class="brand">
      <div class="brand__name">VANTOR</div>
      <div class="brand__tagline">Ridged Concrete &amp; Grinding</div>
    </div>
  </section>

  <section class="card card--back" aria-label="Card back">
    <div class="brand">
      <div class="brand__name">VANTOR</div>
      <div class="brand__tagline">Ridged Concrete &amp; Grinding</div>
    </div>

    <div class="holder">
      <span class="holder__marker"></span>
      <span class="holder__name">Neil Varbusk</span>
    </div>

    <svg class="bands" width="600" height="343" viewBox="0 0 600 343" aria-hidden="true">
      <polygon points="282,236 600,236 600,262 306,262" fill="var(--charcoal)"/>
      <polygon points="0,262 306,262 280,292 0,292" fill="var(--slate)"/>
    </svg>

    <ul class="contacts">
      <li>
        <svg width="18" height="18" viewBox="0 0 18 18"><circle cx="9" cy="9" r="8" fill="none" stroke="#555" stroke-width="1.2"/><path d="M6 5.2c.5-.4 1-.3 1.3.2l.7 1.2c.2.4.1.8-.3 1.1l-.4.3c.5 1.1 1.3 1.9 2.3 2.4l.3-.4c.3-.4.7-.5 1.100-.3l1.2.7c.5.3.5.8.2 1.3-.7.9-1.7 1-2.8.4-1.7-.9-3-2.3-3.8-4-.5-1.100-.3-2.2.2-2.9z" fill="#555"/></svg>
        0491587302
      </li>
      <li>
        <svg width="18" height="18" viewBox="0 0 18 18"><circle cx="9" cy="9" r="8" fill="none" stroke="#555" stroke-width="1.2"/><rect x="4.5" y="6" width="9" height="6.5" fill="#555"/><path d="M4.5 6l4.5 3.6L13.5 6" fill="none" stroke="#fff" stroke-width="0.9"/></svg>
        info@vantorrcg.com.au
      </li>
      <li>
        <svg width="18" height="18" viewBox="0 0 18 18"><circle cx="9" cy="9" r="8" fill="none" stroke="#555" stroke-width="1.2"/><circle cx="9" cy="9" r="4.8" fill="none" stroke="#555" stroke-width="0.9"/><ellipse cx="9" cy="9" rx="2" ry="4.8" fill="none" stroke="#555" stroke-width="0.9"/><path d="M4.2 9h9.6" stroke="#555" stroke-width="0.9"/></svg>
        www.vantorridgedconcrete.com.au
      </li>
    </ul>

    <div class="sectors">Commercial - Domestic - Industrial</div>

    <div class="social">
      <span class="social__chip"></span>
      <span class="social__chip"></span>
      <span class="social__chip"></span>
      <span class="social__handle">/vantorridgedconcrete</span>
    </div>
  </section>

</body>
</html>
```